Brightmark Electrical Flyer

An eye catching flyer design which showcases the type of work we do in the electrical industry in Vancouver,BC. The final design should be simple and incorporate our logo. And present a high end company.

Industry/Entity Type

Electrical

```html
<!DOCTYPE html>
<html lang="en">
<head>
<meta charset="utf-8">
<title>Brightmark Electrical Flyer</title>
<link rel="stylesheet" href="https://fonts.googleapis.com/css2?family=Lato:wght@300;400;700&family=Oswald:wght@300;400&display=swap">
<style>
  :root {
    --yellow: #f2d64b;
    --yellow-deep: #ecc93a;
    --charcoal: #3b3b3b;
    --slate: #58585a;
    --white: #ffffff;
    --page: #ececea;
    --text: #333333;
  }
  * { box-sizing: border-box; margin: 0; padding: 0; }
  html, body { width: 1013px; height: 1200px; overflow: hidden; background: var(--page); }
  body { position: relative; font-family: "Lato", sans-serif; color: var(--text); }

  .card { position: absolute; left: 126px; width: 760px; height: 520px; background: var(--white); overflow: hidden; box-shadow: 0 4px 14px rgba(0,0,0,.18); }
  .card--front { top: 40px; }
  .card--back { top: 640px; }

  /* Front */
  .front-scene { position: absolute; left: 16px; top: 16px; width: 728px; height: 488px; overflow: hidden;
    background: linear-gradient(180deg, #eef2f7 0%, #dfe8f1 35%, #c9d9e4 55%, #d9d6c8 75%, #eef0f2 100%); }
  .front-scene__fade { position: absolute; left: 0; right: 0; bottom: 0; height: 120px; background: linear-gradient(180deg, rgba(255,255,255,0), rgba(255,255,255,.85)); }
  .front-band { position: absolute; left: 0; top: 0; }
  .brand { position: absolute; display: flex; align-items: center; gap: 10px; font-family: "Lato", sans-serif; font-weight: 700; color: var(--charcoal); white-space: nowrap; }
  .brand__dot { width: 26px; height: 26px; border-radius: 50%; background: var(--yellow); flex: none; }
  .front-scene .brand { left: 22px; top: 54px; font-size: 28px; }
  .front-title { position: absolute; left: 18px; top: 400px; font-size: 43px; font-weight: 700; color: var(--charcoal); letter-spacing: .3px; }
  .front-tagline { position: absolute; left: 20px; top: 452px; font-size: 16px; color: var(--charcoal); }
  .web-box { position: absolute; left: 383px; top: 421px; width: 320px; height: 52px; border: 2px solid var(--white); }
  .web-box__fill { position: absolute; left: 9px; top: 6px; right: 12px; bottom: 7px; background: var(--yellow); display: flex; align-items: center; justify-content: center; font-size: 22px; color: var(--charcoal); }

  /* Back */
  .back-photo { position: absolute; left: 320px; top: 0; width: 440px; height: 270px;
    clip-path: polygon(52px 0, 100% 0, 100% 100%, 0 100%);
    background: linear-gradient(160deg, #d9dcdf 0%, #9aa3ab 30%, #4c5258 55%, #7b8790 75%, #c5c9cc 100%); }
  .back-logo-area { position: absolute; left: 0; top: 0; width: 372px; height: 124px; background: var(--white); }
  .back-logo-area .brand { left: 32px; top: 46px; font-size: 30px; }
  .back-rule { position: absolute; left: 0; top: 123px; width: 347px; height: 5px; background: var(--yellow); }
  .about-panel { position: absolute; left: 0; top: 131px; width: 342px; height: 147px; background: var(--slate);
    clip-path: polygon(0 0, 100% 0, 318px 100%, 0 100%);
    color: var(--white); font-weight: 300; font-size: 18.5px; line-height: 24px; padding: 14px 0 0 18px; }
  .offer-text { position: absolute; left: 18px; top: 295px; font-size: 17px; line-height: 22px; color: #444; }
  .services-tab { position: absolute; left: 400px; top: 280px; width: 308px; height: 72px; background: var(--yellow);
    border-radius: 0 0 10px 10px; display: flex; align-items: center; justify-content: center;
    font-family: "Oswald", sans-serif; font-weight: 300; font-size: 33px; color: var(--charcoal); letter-spacing: .5px; }
  .services { position: absolute; left: 0; top: 368px; width: 760px; height: 100px; list-style: none; }
  .service { position: absolute; display: flex; gap: 8px; font-size: 22px; line-height: 22px; color: var(--text); }
  .service svg { flex: none; margin-top: 2px; }
  .footer-rule { position: absolute; left: 0; top: 476px; width: 760px; height: 4px; background: var(--yellow); }
  .footer { position: absolute; left: 0; top: 485px; width: 760px; height: 35px; background: var(--slate); color: var(--white);
    display: flex; align-items: center; justify-content: space-between; padding: 0 28px 0 18px; font-size: 18px; }
</style>
</head>
<body>

<section class="card card--front">
  <div class="front-scene" role="img" aria-label="Photo of a bright modern living room with fireplace, white sofa, striped rug and pool view">
    <div class="front-scene__fade"></div>
  </div>
  <div class="front-scene" style="background:none">
    <svg class="front-band" width="280" height="180" viewBox="0 0 280 180"><polygon points="0,140 266,130 0,172" fill="var(--yellow)"/></svg>
    <div class="brand"><span class="brand__dot"></span>Brightmark Electrical</div>
    <h1 class="front-title">Building Dreams</h1>
    <p class="front-tagline">Expert designers turn your dreams into reality</p>
    <div class="web-box"><div class="web-box__fill">www.brightmarkelectrical.ca</div></div>
  </div>
</section>

<section class="card card--back">
  <div class="back-photo" role="img" aria-label="Photo of an electrical control panel with breakers and coloured wiring"></div>
  <div class="back-logo-area"><div class="brand"><span class="brand__dot"></span>Brightmark Electrical</div></div>
  <div class="back-rule"></div>
  <p class="about-panel">We are an electrical contractor<br>serving the lower mainland.<br>Providing the best in customer<br>service and knowledge,<br>to our clients.</p>
  <p class="offer-text">Brightmark Electrical offers a wide variety<br>of services, to meet your electrical needs.</p>
  <h2 class="services-tab">Types Of Services</h2>

  <svg width="0" height="0" style="position:absolute">
    <symbol id="tick" viewBox="0 0 22 22">
      <rect x="1" y="4" width="16" height="16" rx="3" fill="none" stroke="var(--yellow-deep)" stroke-width="2.4"/>
      <path d="M5 11 L9 15 L20 3" fill="none" stroke="var(--yellow-deep)" stroke-width="3.2" stroke-linecap="round" stroke-linejoin="round"/>
    </symbol>
  </svg>
  <ul class="services">
    <li class="service" style="left:30px;top:0"><svg width="22" height="22"><use href="#tick"/></svg>Residential</li>
    <li class="service" style="left:215px;top:0"><svg width="22" height="22"><use href="#tick"/></svg>Commercial</li>
    <li class="service" style="left:412px;top:0"><svg width="22" height="22"><use href="#tick"/></svg>Lighting</li>
    <li class="service" style="left:574px;top:0"><svg width="22" height="22"><use href="#tick"/></svg>Service</li>
    <li class="service" style="left:30px;top:50px"><svg width="22" height="22"><use href="#tick"/></svg>Fire Alarm</li>
    <li class="service" style="left:215px;top:50px"><svg width="22" height="22"><use href="#tick"/></svg>Low Voltage<br>Wiring</li>
    <li class="service" style="left:412px;top:50px"><svg width="22" height="22"><use href="#tick"/></svg>Security</li>
    <li class="service" style="left:574px;top:50px"><svg width="22" height="22"><use href="#tick"/></svg>Solar Panel</li>
  </ul>
  <div class="footer-rule"></div>
  <footer class="footer"><span>T: 604 555 0147</span><span>info@brightmarkelectrical.ca</span></footer>
</section>

</body>
</html>
```